Real Estate Development Company Stationary

We need our company, business card, letterhead, pocket folder and envelope designed.

We are a new real estate development company. We focus on data centre, commercial and real estate development.

Please see attached for our logo. Since it's a new logo, you still can make minor adjust if you like it makes senses

The client has sent me a business card he really likes. Please see file 3.

Target Market(s)

Real Estate Investors
Large corporations
Home buyers

Industry/Entity Type

Real Estate

```html
<!DOCTYPE html>
<html lang="en">
<head>
<meta charset="utf-8">
<title>Corvale Development Inc. – Business Card</title>
<link rel="stylesheet" href="https://fonts.googleapis.com/css2?family=Didact+Gothic&display=swap">
<style>
  :root {
    --backdrop: #e6e4e0;
    --card-white: #f4f4f4;
    --brand-blue: #173d7e;
    --brand-green: #6aa42f;
    --ink: #333333;
    --rule: #555555;
  }
  * { margin: 0; padding: 0; box-sizing: border-box; }
  html, body {
    width: 1200px; height: 900px; overflow: hidden;
    background: var(--backdrop);
    font-family: "Didact Gothic", "Century Gothic", sans-serif;
  }
  .sheet { position: relative; width: 1200px; height: 900px; }

  .card {
    position: absolute; left: 300px;
    width: 600px; height: 350px;
    box-shadow: 0 6px 18px rgba(0,0,0,0.18);
  }

  /* Card back */
  .card--back { top: 70px; background: var(--brand-blue); overflow: hidden; }
  .card--back .pattern-field {
    position: absolute; inset: 0;
    background: linear-gradient(135deg, #1a4286 0%, #163a79 100%);
  }
  .card--back .wordmark {
    position: absolute; right: 36px; top: 150px;
    color: var(--brand-green); font-size: 30px; letter-spacing: 0.5px;
  }

  /* Card front */
  .card--front { top: 480px; background: var(--card-white); }
  .brand-row {
    position: absolute; left: 40px; top: 40px;
    display: flex; align-items: center; gap: 18px;
  }
  .brand-dot { width: 58px; height: 58px; border-radius: 50%; background: var(--brand-blue); }
  .brand-divider { width: 1px; height: 78px; background: var(--rule); }
  .brand-name { color: var(--brand-green); font-size: 30px; letter-spacing: 0.5px; }

  .contact { position: absolute; left: 40px; top: 146px; color: var(--ink); }
  .contact__name { font-size: 26px; margin-bottom: 10px; }
  .contact__role { font-size: 15px; margin-left: 10px; }
  .contact__line { font-size: 14px; line-height: 21px; }
  .contact__label { color: var(--brand-blue); margin-right: 4px; }
  .contact__spacer { display: inline-block; width: 14px; }
  .contact__address { margin-top: 10px; }
  .contact__web { color: var(--brand-blue); }

  .card--front .band {
    position: absolute; left: 0; right: 0; bottom: 14px; height: 20px;
    background: var(--brand-blue);
  }
</style>
</head>
<body>
<main class="sheet">
  <section class="card card--back" aria-label="Business card back">
    <div class="pattern-field" role="img" aria-label="Repeating interlocked brand-symbol pattern in deep blue tones"></div>
    <div class="wordmark">Corvale Development Inc.</div>
  </section>

  <section class="card card--front" aria-label="Business card front">
    <div class="brand-row">
      <div class="brand-dot"></div>
      <div class="brand-divider"></div>
      <div class="brand-name">Corvale Development Inc.</div>
    </div>
    <div class="contact">
      <p class="contact__name">Lukas Brenner<span class="contact__role">CEO</span></p>
      <p class="contact__line"><span class="contact__label">PHONE</span>+41 56 210 48 63<span class="contact__spacer"></span><span class="contact__label">MOBILE</span>+41 79 384 26 17</p>
      <p class="contact__line"><span class="contact__label">EMAIL</span>lukas.brenner@corvaledev.com</p>
      <p class="contact__line contact__address">Lindenweg 12, 5400 Baden, Switzerland</p>
      <p class="contact__line contact__web">www.corvaledev.com</p>
    </div>
    <div class="band"></div>
  </section>
</main>
</body>
</html>
```